Book cover design : The Copper Lantern

We need a striking book cover design for a book which will be published via Orvello Reader and as a paperback. The book is a simple short story - ghost story - for children. The book is set in a contemporary English town.

The title of the book is : The Copper Lantern
The author is: Walter Finch

The book is a story book, for children, aged approximately 11-15 years old.
It is a ghost story, but not too scary.

Text to go on the front cover:
The Copper Lantern

Walter Finch

Text to go on the back cover :

The Copper Lantern; a ghost story of controlled readability for students aged 11 to 15 years, (catch-up reading). Also for students of English as a foreign language.

Target Market(s)

A ghost story of controlled readability for students aged 11 to 15 years, (catch-up reading). Also for students of English as a foreign language.

```html
<!DOCTYPE html>
<html lang="en">
<head>
<meta charset="UTF-8">
<title>The Copper Lantern – Book Cover</title>
<link rel="stylesheet" href="https://fonts.googleapis.com/css2?family=Archivo+Black&family=Oswald:wght@700&family=Open+Sans:wght@400;800&display=swap">
<style>
  :root {
    --page-bg: #f1f1f2;
    --cover-top: #dcdae0;
    --cover-mid: #c9c8d0;
    --cover-bottom: #a4a6b8;
    --back-top: #b3b2bf;
    --back-bottom: #9c9daf;
    --accent-red: #ee1111;
    --title-white: #f4f4f6;
    --glitch-cyan: #2fe4ef;
    --glitch-magenta: #e02ad8;
    --hand-tone: rgba(120, 104, 110, 0.55);
  }
  * { margin: 0; padding: 0; box-sizing: border-box; }
  html, body {
    width: 1200px;
    height: 800px;
    overflow: hidden;
    background: var(--page-bg);
  }
  .spread {
    position: absolute;
    top: 110px;
    left: 200px;
    display: flex;
    gap: 40px;
  }
  .cover {
    position: relative;
    width: 380px;
    height: 560px;
    overflow: hidden;
    box-shadow: 0 10px 30px rgba(0, 0, 0, 0.12);
  }

  /* Back cover */
  .cover--back {
    background: linear-gradient(170deg, var(--back-top), var(--back-bottom));
    color: var(--title-white);
    font-family: "Open Sans", sans-serif;
    padding: 62px 44px 0;
  }
  .back-title {
    font-weight: 800;
    font-size: 23px;
    text-align: center;
    white-space: nowrap;
    letter-spacing: 0.3px;
    margin-bottom: 36px;
  }
  .back-blurb,
  .back-body {
    font-size: 10px;
    line-height: 1.6;
    margin-bottom: 16px;
  }

  /* Front cover */
  .cover--front {
    background: linear-gradient(180deg, var(--cover-top) 0%, var(--cover-mid) 55%, var(--cover-bottom) 100%);
  }
  .author {
    position: absolute;
    top: 40px;
    left: 34px;
    font-family: "Archivo Black", sans-serif;
    color: var(--accent-red);
    font-size: 17px;
    line-height: 1.15;
    letter-spacing: 1.5px;
    text-transform: uppercase;
  }
  .hand-photo {
    position: absolute;
    top: 170px;
    left: 70px;
    width: 230px;
    height: 280px;
  }
  .title {
    position: absolute;
    left: 72px;
    top: 330px;
    font-family: "Oswald", sans-serif;
    font-weight: 700;
    text-transform: uppercase;
    line-height: 0.95;
  }
  .title__the {
    display: block;
    font-size: 58px;
    color: transparent;
    -webkit-text-stroke: 2px var(--title-white);
  }
  .title__main {
    display: block;
    font-size: 62px;
    color: var(--title-white);
    margin-left: 40px;
    text-shadow: -3px 0 0 var(--glitch-cyan), 3px 0 0 var(--glitch-magenta);
  }
  .title__sub {
    display: block;
    font-size: 54px;
    color: var(--accent-red);
    margin-left: 28px;
  }
</style>
</head>
<body>
  <main class="spread">
    <section class="cover cover--back" aria-label="Back cover">
      <h2 class="back-title">THE COPPER LANTERN</h2>
      <p class="back-blurb">The Copper Lantern; a ghost story of controlled readability for students aged 11 to 15 years, (catch-up reading). Also for students of English as a foreign language.</p>
      <p class="back-body">Lorem ipsum dolor sit amet, consectetur adipiscing elit, sed do eiusmod tempor incididunt ut labore et dolore magna aliqua. Quis ipsum suspendisse ultrices gravida. Risus commodo viverra maecenas accumsan lacus vel facilisis. Lorem ipsum dolor sit amet, sed do eiusmod tempor incididunt ut labore.</p>
      <p class="back-body">Lorem ipsum dolor sit amet, consectetur adipiscing elit, sed do eiusmod tempor incididunt ut labore et dolore magna aliqua. Risus commodo viverra lacus vel facilisis.</p>
      <p class="back-body">Lorem ipsum dolor sit amet, consectetur adipiscing elit, sed do eiusmod tempor incididunt ut labore et dolore magna aliqua. Quis ipsum suspendisse ultrices gravida. Risus commodo viverra maecenas accumsan lacus vel facilisis. Lorem ipsum dolor sit amet, sed do eiusmod tempor incididunt ut labore. Quis ipsum suspendisse ultrices gravida. Risus commodo accumsan lacus vel facilisis.</p>
    </section>

    <section class="cover cover--front" aria-label="Front cover">
      <p class="author">Walter<br>Finch</p>
      <svg class="hand-photo" role="img" aria-label="Blurred photograph of a hand pressed against frosted glass" viewBox="0 0 230 280">
        <defs>
          <radialGradient id="handGlow" cx="50%" cy="45%" r="50%">
            <stop offset="0%" stop-color="var(--hand-tone)"/>
            <stop offset="100%" stop-color="rgba(200,198,206,0)"/>
          </radialGradient>
        </defs>
        <rect width="230" height="280" fill="url(#handGlow)"/>
      </svg>
      <h1 class="title">
        <span class="title__the">The</span>
        <span class="title__main">Copper</span>
        <span class="title__sub">Lantern</span>
      </h1>
    </section>
  </main>
</body>
</html>
```